Corvina Heights A3 Poster

An A3 Poster is needed for a Preview Open Day for Corvina Heights.

A3, full colour, single sided, bleed to edge.

Corvina Heights is a residential development located in Wagga Wagga in Australia, which is 6 hours west of Sydney. They are currently selling blocks of land. There is nothing currently built on the site yet. They are holding a preview open day for the locals and prospective buyers to attend to learn more about the development as well as have a fun family day out.

The objective is to excite people to want to attend this fun family day event.
Updates

Please make the poster more "fun" as we are promoting one day filled with family fun activities.

Please move the text around if you think it will work better. and please use images of young families or children with balloons or face painting - having fun.

Thank you

Industry/Entity Type

Residential

Requirements
Must have
• Logo
• Tagline 'Simply the best' (currently being used)
• Copy (the order of copy can be altered to suit poster)
Nice to have
• There is a brochure called Heritage Almanac which has been uploaded which we like the look and feel. This is currently a communication piece which is being distributed from Tallowmere Shire Board. Although it cannot be replicated we would like to use this as inspiration to compliment this poster.
• There is a link to some current photography which can be used if relevant. We are also open to suggestions on other photography.
• The link is here:
• https://www.filevaultex.com/sh/7qmtrelkpwzdv/KpRt3Hx9Lq
• Balanced amount of fonts

```html
<!DOCTYPE html>
<html lang="en">
<head>
<meta charset="utf-8">
<title>Corvina Heights – Preview Open Day Poster</title>
<link rel="stylesheet" href="https://fonts.googleapis.com/css2?family=Marcellus&family=Alegreya:wght@400&family=Oswald:wght@500;700&family=Arimo&display=swap">
<style>
  :root {
    --sky-deep: #0f5a9c;
    --sky-light: #2a8fd6;
    --sun: #fff27a;
    --grass: #8dbb4c;
    --brand-blue: #17639c;
    --slate-grey: #8f8f8f;
    --navy: #0e2347;
    --panel-blue: rgba(20, 86, 145, 0.95);
    --footer-dark: #0b3c6e;
    --footer-light: #1683cc;
    --white: #ffffff;
  }
  * { margin: 0; padding: 0; box-sizing: border-box; }
  html, body { width: 1200px; height: 1000px; overflow: hidden; background: var(--white); }
  .poster {
    position: absolute; left: 290px; top: 22px;
    width: 669px; height: 949px; overflow: hidden; background: var(--white);
  }
  .photo-backdrop {
    position: absolute; left: 0; top: 560px; width: 669px; height: 340px; z-index: 0;
    background: linear-gradient(to bottom, rgba(255,255,255,1) 0%, #e6ebe7 12%, #a9c08f 42%, #6f9b3e 60%, #4d4a42 80%, #2b2824 100%);
  }
  .sky-band { position: absolute; left: 0; top: 0; width: 669px; height: 200px; }
  .join-heading {
    position: absolute; right: 60px; top: 66px; z-index: 1;
    font-family: "Marcellus", serif; font-weight: 400; font-size: 40px; color: var(--white); letter-spacing: 1px;
  }
  .brand-name {
    position: absolute; left: 0; width: 669px; top: 172px; text-align: center; z-index: 1;
    font-family: "Marcellus", serif; font-weight: 400; font-size: 76px; color: var(--brand-blue); line-height: 1;
    padding-left: 18px;
  }
  .brand-place {
    position: absolute; right: 44px; top: 262px; z-index: 1;
    font-family: "Marcellus", serif; font-weight: 400; font-size: 34px; color: var(--slate-grey); letter-spacing: 3px;
  }
  .event-title {
    position: absolute; left: 0; width: 669px; top: 310px; text-align: center; z-index: 1;
    font-family: "Oswald", sans-serif; font-weight: 700; font-size: 56px; color: var(--grass);
    line-height: 1; transform: scaleX(1.05);
  }
  .event-date {
    position: absolute; left: 0; width: 669px; top: 371px; text-align: center; z-index: 1;
    font-family: "Oswald", sans-serif; font-weight: 700; font-size: 20px; color: var(--navy);
    letter-spacing: 12px; line-height: 1; padding-left: 12px;
  }
  .event-time {
    position: absolute; left: 0; width: 669px; top: 402px; text-align: center; z-index: 1;
    font-family: "Oswald", sans-serif; font-weight: 500; font-size: 22px; color: var(--navy);
    letter-spacing: 2px; line-height: 1;
  }
  .event-copy {
    position: absolute; left: 20px; width: 629px; top: 444px; text-align: center; z-index: 1;
    font-family: "Alegreya", serif; font-size: 15.5px; color: var(--navy); line-height: 28px;
  }
  .fun-heading {
    position: absolute; left: 0; width: 669px; top: 566px; text-align: center; z-index: 1;
    font-family: "Arimo", sans-serif; font-weight: 400; font-size: 24px; color: var(--navy);
  }
  .activity-list {
    position: absolute; left: 62px; top: 622px; list-style: none; z-index: 1;
    font-family: "Alegreya", serif; font-size: 15.5px; color: var(--navy); line-height: 23px;
  }
  .activity-list li::before { content: "•"; display: inline-block; width: 20px; }
  .snapshot {
    position: absolute; background: var(--white); padding: 6px 6px 14px; z-index: 1;
    box-shadow: 0 2px 5px rgba(0,0,0,0.3);
  }
  .snapshot-fill { width: 100%; height: 100%; }
  .snapshot-face { left: 240px; top: 632px; width: 78px; height: 110px; transform: rotate(-6deg); }
  .snapshot-face .snapshot-fill { background: linear-gradient(135deg, #e3a04a, #c2552e); }
  .snapshot-castle { left: 302px; top: 614px; width: 98px; height: 84px; transform: rotate(-9deg); }
  .snapshot-castle .snapshot-fill { background: linear-gradient(160deg, #7fbf5a, #3f8a38); }
  .snapshot-picnic { left: 296px; top: 676px; width: 80px; height: 94px; }
  .snapshot-picnic .snapshot-fill { background: linear-gradient(160deg, #9cbf8a, #b08a6a); }
  .info-panel {
    position: absolute; left: 439px; top: 638px; width: 230px; height: 162px; z-index: 1;
    background: var(--panel-blue); border-radius: 6px 0 0 6px;
    font-family: "Alegreya", serif; font-size: 10px; color: var(--white); line-height: 11px;
    padding: 10px 12px 0 14px;
  }
  .info-panel p { margin-bottom: 11px; }
  .info-lead { text-align: center; }
  .footer-band {
    position: absolute; left: 0; bottom: 0; width: 669px; height: 56px; z-index: 1;
    background: linear-gradient(to right, var(--footer-dark), var(--footer-light));
    font-family: "Marcellus", serif; font-size: 20px; color: var(--white);
    letter-spacing: 12px; text-align: center; line-height: 56px;
  }
</style>
</head>
<body>
<main class="poster">
  <div class="photo-backdrop" role="img" aria-label="Sunny park lawn with a barbecue grill of sausages, corn and skewers in the foreground"></div>

  <svg class="sky-band" viewBox="0 0 669 200" role="img" aria-label="Blue sky with a bright rising sun and sunburst over a green hill">
    <defs>
      <linearGradient id="skyGradient" x1="0" y1="0" x2="1" y2="1">
        <stop offset="0" stop-color="#2a8fd6"/>
        <stop offset="1" stop-color="#0f5a9c"/>
      </linearGradient>
      <radialGradient id="sunGlow" cx="0.2" cy="0.78" r="0.45">
        <stop offset="0" stop-color="#ffffff"/>
        <stop offset="0.15" stop-color="#fff27a"/>
        <stop offset="0.5" stop-color="#f2e77a" stop-opacity="0.5"/>
        <stop offset="1" stop-color="#2a8fd6" stop-opacity="0"/>
      </radialGradient>
    </defs>
    <rect width="669" height="200" fill="url(#skyGradient)"/>
    <rect width="669" height="200" fill="url(#sunGlow)"/>
    <path d="M0 168 C160 125 440 120 669 168 L669 200 L0 200 Z" fill="#8dbb4c"/>
    <path d="M0 176 C160 134 440 129 669 176 L669 200 L0 200 Z" fill="#ffffff"/>
  </svg>
  <div class="join-heading">JOIN US AT</div>

  <h1 class="brand-name">Corvina Heights</h1>
  <div class="brand-place">WAGGA WAGGA</div>

  <h2 class="event-title">PREVIEW OPEN DAY</h2>
  <div class="event-date">Saturday 28 September</div>
  <div class="event-time">10am – 2pm</div>

  <div class="event-copy">
    Come along &amp; see Wagga Wagga’s newest land release<br>
    Meet the Project Team, talk with leading local builders, banks, and solicitors on the day.<br>
    Gather all the information you need to start building your new dream home with your choice<br>
    of builder and design at Corvina Heights
  </div>

  <h3 class="fun-heading">Enjoy free family fun activities!</h3>

  <ul class="activity-list">
    <li>Free BBQ</li>
    <li>Jumping Castle</li>
    <li>Face Painting</li>
    <li>3KR broadcasting live</li>
    <li>plus more...</li>
  </ul>

  <div class="snapshot snapshot-castle"><div class="snapshot-fill" role="img" aria-label="Photo of a bouncy jumping castle on the grass"></div></div>
  <div class="snapshot snapshot-face"><div class="snapshot-fill" role="img" aria-label="Photo of a child with face paint"></div></div>
  <div class="snapshot snapshot-picnic"><div class="snapshot-fill" role="img" aria-label="Photo of families sharing a picnic table"></div></div>

  <aside class="info-panel">
    <p class="info-lead">Register your interest today &amp; learn about the early bird offer with land from $112,500</p>
    <p>Visit corvinaheights.com.au<br>Or Contact: Hollis Brandt M 0400555019 E hollis@brightlotpb.com.au</p>
    <p>Corvina Heights New Land Release<br>Just 5 minutes north of the CBD head over the Marrowgate Bridge, turn left in to Old Kestrel Road and turn right in to Fern Hollow Road</p>
  </aside>

  <footer class="footer-band">corvinaheights.com.au</footer>
</main>
</body>
</html>
```